Alaska Law Firm Needs a Sticker Design

We need a design for stickers to put on already-printed brochures. We mail the brochures to potential clients so they can learn more about accident-induced injuries, insurance claims, legal representation, and our own law firm.

One of our lawyers wrote a book that provides a helpful overview of personal injury claims. We are offering this book for free to anyone who calls and requests it. Therefore, the sticker design should include one of the following phrases, or something very similar:
a) "Still have questions? Call and request our book-- for free!"
b) "Still have questions about auto accident claims? Call and request our book today."
c) "Still have questions about filing a claim? Call and request a free copy of our book."
d) "Still have questions? Call us today to request a free copy of our book, Clear Lanes Ahead."
e) "To learn more about automobile accidents and insurance, call today and request a free copy of our book."

The sticker should be approximately 3"x3" and may be a circle, square, rectangle, or ellipsis. The sticker will be placed on the back of the folder, which is light blue. We would like the sticker to match the color scheme of our website and the folder.

I will upload an image of the book cover as soon as I obtain it.

Industry/Entity Type

Law Firm

Font styles to use
Serif
Sans Serif

Requirements
Should not have
• Bright colors that aren't already used in the folder design. e.g. no bright orange, pink, chartreuse, turquoise, yellow, red.

```html
<!DOCTYPE html>
<html lang="en">
<head>
<meta charset="utf-8">
<title>Still Have Questions? Sticker</title>
<link rel="stylesheet" href="https://fonts.googleapis.com/css2?family=Source+Sans+3:wght@700;800&display=swap">
<style>
  :root {
    --navy: #17416b;
    --paper: #ffffff;
    --silver: #c9c9c9;
  }
  html, body {
    margin: 0;
    padding: 0;
    width: 1200px;
    height: 1200px;
    overflow: hidden;
    background: var(--paper);
  }
  .sticker {
    display: block;
    width: 1200px;
    height: 1200px;
  }
  .sticker__disc { fill: var(--navy); }
  .sticker__corner { fill: var(--paper); }
  .sticker text {
    font-family: "Source Sans 3", "Myriad Pro", Arial, sans-serif;
    font-weight: 700;
  }
  .headline { fill: var(--paper); }
  .headline--small { font-size: 140px; }
  .headline--large { font-size: 212px; font-weight: 800; }
  .offer { fill: var(--silver); font-size: 126px; }
  .free-tag { fill: var(--navy); }
  .free-tag--for { font-size: 132px; }
  .free-tag--free { font-size: 250px; font-weight: 800; }
</style>
</head>
<body>
  <svg class="sticker" viewBox="0 0 1200 1200" xmlns="http://www.w3.org/2000/svg" role="img" aria-label="Still have questions? Call and request our book for free">
    <circle class="sticker__disc" cx="600" cy="600" r="598"/>
    <path class="sticker__corner" d="M 405 1200 L 405 1172 C 470 900 640 735 860 732 C 1000 730 1120 775 1200 820 L 1200 1200 Z"/>

    <text class="headline headline--small" x="260" y="327" textLength="687" lengthAdjust="spacingAndGlyphs">STILL HAVE</text>
    <text class="headline headline--large" x="127" y="527" textLength="946" lengthAdjust="spacingAndGlyphs">QUESTIONS?</text>

    <text class="offer" x="117" y="700" textLength="822" lengthAdjust="spacingAndGlyphs">Call and request</text>
    <text class="offer" x="117" y="833" textLength="449" lengthAdjust="spacingAndGlyphs">our book</text>

    <g class="free-tag" transform="rotate(-35 700 900)">
      <text class="free-tag free-tag--for" x="585" y="905" textLength="230" lengthAdjust="spacingAndGlyphs">FOR</text>
    </g>
    <g class="free-tag" transform="rotate(-35 800 1010)">
      <text class="free-tag free-tag--free" x="570" y="1095" textLength="470" lengthAdjust="spacingAndGlyphs">FREE</text>
    </g>
  </svg>
</body>
</html>
```